PPE EQIUPMENT

WE WOULD LIKE TO PRODUCE 2 DIFFERENT BANNERS TO BE PLACED OUTSIDE OF OUR WAREHOUSE TO ADVERTISE THAT WE HAVE FACE MASKS, HAND SANITISERS, DISINFECTANT SPRAY, FACE SHIELDS AND HAND SOAP. THE SIZE OF EACH BANNER WILL BE , portrait to be (W) 140 cm x (H) 250 cm, with 4 x eyelets. THE BANNER IS TO STATE PPE EQUIPMENT AVAILABLE HERE AND SHOW OUR PHONE NUMBER 0207-946-0318. FINALLY WE WILL REQUIRE SOME IMAGES OF THE PRODUCTS IF YOU CAN SUPPLY THESE. THANKS

```html
<!DOCTYPE html>
<html lang="en">
<head>
<meta charset="utf-8">
<title>PPE Available Here – Banner</title>
<link href="https://fonts.googleapis.com/css2?family=Source+Sans+3:wght@700;800&display=swap" rel="stylesheet">
<style>
  :root {
    --lime: #bccf02;
    --ink: #0d0d0d;
    --white: #ffffff;
    --shield-tone: linear-gradient(160deg, #dfe9f2 0%, #9fb9d4 100%);
    --mask-tone: linear-gradient(160deg, #5fb5b3 0%, #2f7f86 100%);
    --soap-tone: linear-gradient(180deg, #e6eef5 0%, #c9d9e6 60%, #e58aa8 100%);
    --spray-tone: linear-gradient(180deg, #f2f4f5 0%, #cfe3e6 100%);
    --sanitiser-tone: linear-gradient(170deg, #d7ecf7 0%, #8cc3e3 100%);
  }
  * { margin: 0; padding: 0; box-sizing: border-box; }
  html, body { width: 673px; height: 1200px; overflow: hidden; background: var(--lime); }
  .banner {
    position: relative;
    width: 673px;
    height: 1200px;
    background: var(--lime);
    font-family: "Source Sans 3", "Helvetica Neue", Arial, sans-serif;
    color: var(--ink);
    border: 3px solid var(--white);
  }
  .headline {
    position: absolute;
    top: 50px;
    left: 0;
    width: 100%;
    text-align: center;
    font-weight: 800;
    font-size: 104px;
    line-height: 88px;
    letter-spacing: -1px;
  }
  .product-visual { position: absolute; }
  .product-label {
    position: absolute;
    text-align: center;
    font-weight: 800;
    font-size: 28px;
    line-height: 30px;
    white-space: nowrap;
    transform: translateX(-50%);
  }
  .face-shield { left: 85px; top: 346px; width: 176px; height: 204px; background: var(--shield-tone); border-radius: 60px 60px 18px 18px; }
  .face-mask { left: 374px; top: 364px; width: 204px; height: 180px; background: var(--mask-tone); border-radius: 50% 50% 40% 40%; }
  .hand-soap { left: 63px; top: 636px; width: 135px; height: 218px; background: var(--soap-tone); border-radius: 30px 30px 22px 22px; }
  .disinfectant-spray { left: 270px; top: 646px; width: 76px; height: 208px; background: var(--spray-tone); border-radius: 20px 20px 14px 14px; }
  .hand-sanitiser { left: 423px; top: 607px; width: 198px; height: 247px; background: var(--sanitiser-tone); border-radius: 24px; }

  .phone {
    position: absolute;
    top: 976px;
    left: 0;
    width: 100%;
    text-align: center;
    font-weight: 800;
    font-size: 61px;
    line-height: 70px;
  }
  .company-name {
    position: absolute;
    top: 1094px;
    left: 0;
    width: 100%;
    text-align: center;
    font-weight: 800;
    font-size: 36px;
    line-height: 44px;
    color: var(--ink);
  }
</style>
</head>
<body>
  <main class="banner">
    <h1 class="headline">PPE<br>Available<br>Here</h1>

    <div class="product-visual face-shield" role="img" aria-label="Photo of a clear face shield worn over a surgical mask"></div>
    <div class="product-label" style="left:162px; top:556px;">Face Shield</div>

    <div class="product-visual face-mask" role="img" aria-label="Photo of a teal respirator face mask"></div>
    <div class="product-label" style="left:476px; top:556px;">Face Mask</div>

    <div class="product-visual hand-soap" role="img" aria-label="Photo of a pump bottle of hand soap"></div>
    <div class="product-label" style="left:128px; top:866px;">Hand Soap</div>

    <div class="product-visual disinfectant-spray" role="img" aria-label="Photo of a disinfectant spray bottle"></div>
    <div class="product-label" style="left:310px; top:866px;">Disinfectant<br>Spray</div>

    <div class="product-visual hand-sanitiser" role="img" aria-label="Photo of two blue bottles of hand sanitiser"></div>
    <div class="product-label" style="left:525px; top:866px;">Hand Sanetiser</div>

    <p class="phone">Ph.: 0207-946-0318.</p>

    <p class="company-name">Kingsway Furniture</p>
  </main>
</body>
</html>
```